Project Management - Web Design Project

Vantrel 4 Management Limited is a company which provides specialist Project Control and Contract Management expertise to the Engineering, Construction and Manufacturing industries. The emphasis is on advanced Project Management techniques in particular Planning & Scheduling, Cost Control, Change Control, Risk Management, Reporting and Contract Administration. We are a global company (albeit a small start-up at this time) and pride ourselves on our ability to support projects to help them achieve their goals and objectives. Our aim is to implement work class control tools in a simple and user friendly manner. We would like the website to appear professional but at the same time easy to navigate and a good balance between text and pictures. The final design should communicate our value added service to our customers, our willingness to support and our structured approach to our work.

Target Market(s)

Project Management professionals working for engineering, construction and manufacturing organisations involved with delivering projects.

Industry/Entity Type

Construction

Requirements
Must have
• The website must include all of the content from the attached Excel brief. The company logo (attached) must also be included in the design. The design must portray a professional look and feel. Please include pictures and photographs related to project management in the engineering, construction and manufacturing industries. We may supplement with pictures of our own during the next steps.
Nice to have
• Emphasis that Vantrel 4 is available to support, guide, direct to achieve positive outcomes for the projects. We work hard at developing our customer relationships. Our employees are experienced in advanced project management techniques.
Should not have
• The design should not use old style fonts. It should look modern and professional. Do not include cartoons or silly illustrations.

```html
<!DOCTYPE html>
<html lang="en">
<head>
<meta charset="utf-8">
<title>Vantrel 4 Management Limited</title>
<link rel="stylesheet" href="https://fonts.googleapis.com/css2?family=Ubuntu:wght@300;400;500;700&family=Roboto:wght@400&display=swap">
<style>
:root{
  --blue:#1f6fc6;
  --blue-link:#2a73c9;
  --blue-panel:rgba(96,160,238,.85);
  --text-grey:#7d7d7d;
  --dark-grey:#555;
  --header-bg:#f4f0e6;
  --nav-dark:#4a3f38;
  --nav-light:#6b5d53;
  --footer-bg:#111;
  --rule:#e3ded3;
}
*{box-sizing:border-box;margin:0;padding:0}
html,body{width:1200px;height:1190px;overflow:hidden}
body{position:relative;background:#fbfaf6;font-family:"Ubuntu",sans-serif;color:var(--text-grey)}
.site-header{position:absolute;left:0;top:0;width:1200px;height:168px;background:linear-gradient(#f7f4ec,#efeadf);border-top:4px solid #3d3d3d;border-bottom:1px solid var(--rule)}
.brand{position:absolute;left:118px;top:24px;width:165px;text-align:center}
.brand-mark{width:74px;height:74px;border-radius:50%;background:#2c7ad6;margin:0 auto 8px}
.brand-name{font-weight:500;font-size:13px;line-height:15px;color:#5a5a5a;letter-spacing:1px;text-transform:uppercase}
.callout{position:absolute;left:692px;top:14px;display:flex;align-items:center;gap:12px;font-weight:300;font-size:17px;color:var(--blue-link)}
.callout strong{font-weight:500}
.main-nav{position:absolute;left:386px;top:95px;width:705px;height:46px;border-radius:4px;background:linear-gradient(var(--nav-light),var(--nav-dark));display:flex;align-items:center;justify-content:space-between;padding:0 12px 0 14px;border:1px solid #3a322d}
.main-nav a{color:#f3efe8;font-weight:300;font-size:15px;text-decoration:none}
.main-nav a.active{font-weight:700;text-transform:uppercase;font-size:14px}
.hero{position:absolute;left:0;top:168px;width:1200px;height:453px;background:linear-gradient(90deg,#fbfbfb 0%,#f1f3f5 40%,#dfe5ea 65%,#4c5f8a 82%,#6d7a8c 100%)}
.hero-photo{position:absolute;inset:0}
.hero-panel{position:absolute;left:111px;top:100px;width:487px;height:209px;border-radius:5px;background:var(--blue-panel);padding:16px 13px;color:#fff}
.hero-panel h1{font-weight:500;font-size:26px;margin-bottom:18px}
.hero-panel p{font-weight:300;font-size:13.5px;line-height:17px;margin-bottom:16px;letter-spacing:-.2px}
.hero-panel a{color:#0d1e3a;font-size:15px;text-decoration:underline}
.content{position:absolute;left:0;top:621px;width:1200px;height:501px;background:linear-gradient(#f4efe0 0,#fbfaf6 60px)}
.section-title{font-weight:400;font-size:23px;color:var(--blue)}
.prime{position:absolute;left:112px;top:26px;width:630px}
.prime p{margin-top:12px;font-weight:300;font-size:14px;line-height:18px;color:var(--text-grey)}
.divider{position:absolute;left:764px;top:18px;width:1px;height:470px;background:var(--rule)}
.deliverables{position:absolute;left:802px;top:26px}
.deliverables ul{list-style:none;margin-top:10px;margin-left:-10px}
.deliverables li{font-weight:300;font-size:14.5px;line-height:24px;color:var(--blue-link)}
.deliverables li::before{content:"•";margin-right:5px}
.feature{position:absolute;top:271px;width:268px}
.feature-frame{width:268px;height:129px;border:1px solid #ddd;background:#fff;padding:5px;box-shadow:0 1px 3px rgba(0,0,0,.08)}
.feature-photo{width:100%;height:100%}
.feature h3{font-weight:400;font-size:14px;color:var(--blue-link);margin:12px 0 5px 6px}
.feature p{font-size:13px;line-height:15.5px;color:var(--text-grey);margin-left:6px;letter-spacing:.2px}
.news{position:absolute;left:796px;top:262px;width:296px;font-family:"Roboto",sans-serif}
.news h2{font-family:"Ubuntu",sans-serif;font-weight:400;font-size:19px;color:var(--dark-grey);margin-bottom:24px}
.news-item{display:flex;gap:15px;height:90px;border-bottom:1px solid var(--rule);margin-bottom:16px}
.news-item:last-child{border:0}
.date{width:42px;text-align:center}
.date .day{display:block;width:40px;height:34px;border:1px solid #ddd;background:#fff;font-weight:700;font-size:20px;line-height:32px;color:#555;box-shadow:0 1px 2px rgba(0,0,0,.1)}
.date .month{font-size:10px;color:#999;display:block;margin-top:6px}
.news-body h4{font-weight:400;font-size:14px;color:#444}
.news-body p{font-size:12px;color:#888;margin-top:3px}
.site-footer{position:absolute;left:0;top:1122px;width:1200px;height:68px;background:var(--footer-bg);font-family:"Roboto",sans-serif}
.copyright{position:absolute;left:116px;top:19px;font-size:12px;color:#ccc}
.legal{position:absolute;left:124px;top:37px;font-size:12px;color:#888}
.legal a{color:#5aa2ec;text-decoration:none}
.social{position:absolute;left:900px;top:18px;display:flex;gap:10px;align-items:center}
.social .dot{width:24px;height:24px;border-radius:50%;background:#eee}
</style>
</head>
<body>
<header class="site-header">
  <div class="brand">
    <div class="brand-mark"></div>
    <div class="brand-name">Vantrel 4<br>Management Limited</div>
  </div>
  <div class="callout">
    <svg width="22" height="22" viewBox="0 0 24 24" aria-hidden="true"><path fill="#555" d="M6.6 10.8a15.1 15.1 0 0 0 6.6 6.6l2.2-2.2c.3-.3.7-.4 1-.2 1.1.4 2.3.6 3.6.6.6 0 1 .4 1 1V20c0 .6-.4 1-1 1A17 17 0 0 1 3 4c0-.6.4-1 1-1h3.5c.6 0 1 .4 1 1 0 1.3.2 2.5.6 3.6.1.3 0 .7-.2 1z"/></svg>
    <span>For a FREE &nbsp;call to contact us on : <strong>0144 555 0192</strong></span>
  </div>
  <nav class="main-nav">
    <a class="active" href="#">Home</a>
    <a href="#">Why work with us?</a>
    <a href="#">Services</a>
    <a href="#">Our sales Process</a>
    <a href="#">FAQs</a>
    <a href="#">Proven Success</a>
    <a href="#">News</a>
  </nav>
</header>

<section class="hero">
  <div class="hero-photo" role="img" aria-label="Smiling engineer in blue overalls at a desk with a hard hat, drawings and laptop in a bright office"></div>
  <div class="hero-panel">
    <h1>Managemnent Limited</h1>
    <p>Effective Contract Management is essential for a project to be success-ful. &nbsp;The contract represents the agreed rights and obligations made by each party to one anolther. &nbsp;In addition there may be many underlying obligations some stated explicitly in the contract while others may be implied. These obligations form the baseline frame of reference.</p>
    <a href="#">Learn more about Vantrel 4 Management Limited</a>
  </div>
</section>

<main class="content">
  <section class="prime">
    <h2 class="section-title">Prime Contract Administration</h2>
    <p>Depending on the contracting arrangement adopted by the contractor certain scope may be sub con-tracted to a third party (sub contractor / supplier) due to the specialist nature of the work. &nbsp;In many instances the amount of work sub contracted may in fact exceed the work to be performed directly by the principal contractor. &nbsp;While the work may be sub contracted on a lump sum basis, it remains vital to the project team to manage these sub contractors to ensure a successful outcome for the project. &nbsp;Sub contract management (administration) is often a complex and time consuming task especially if the systems and processes needed are not sufficiently mature. &nbsp;Our approach is to equip the project team with these systems and processes, procedures and tools to enable them to quickly implement the control required without expending a significant time developing a sub contract administration system.</p>
  </section>

  <div class="divider"></div>

  <section class="deliverables">
    <h2 class="section-title">Sub Contractor Deliverables</h2>
    <ul>
      <li>Contract Baseline Schedule</li>
      <li>Monthly Reporting Requirements</li>
      <li>Site Instructions</li>
      <li>Requests for Information (RFI)</li>
      <li>Change Requests</li>
      <li>Mobilisation Plan</li>
      <li>Resource Plans</li>
    </ul>
  </section>

  <article class="feature" style="left:111px">
    <div class="feature-frame"><div class="feature-photo" role="img" aria-label="Team of colleagues reviewing work together at a desk" style="background:linear-gradient(90deg,#8a9bb0,#d9d4cc 50%,#6f7f95)"></div></div>
    <h3>General</h3>
    <p>Contract Appraisal Meeting &nbsp;&nbsp;Responsibil-ity Assignment Matrix Customer Supplied Deliverables</p>
  </article>

  <article class="feature" style="left:415px">
    <div class="feature-frame"><div class="feature-photo" role="img" aria-label="Business professionals in a bright meeting room" style="background:linear-gradient(90deg,#3e4550,#c9ccd1 55%,#4a5260)"></div></div>
    <h3>Claims &amp; Dispute</h3>
    <p>Schedule Claims Analysis Schedule Impact Management Notices and Claim Preparation</p>
  </article>

  <section class="news">
    <h2>Upcoming News</h2>
    <div class="news-item">
      <div class="date"><span class="day">16</span><span class="month">SEP</span></div>
      <div class="news-body"><h4>Sunday Services</h4><p>Harbourton, Maple Row</p><p>08:45 AM</p></div>
    </div>
    <div class="news-item">
      <div class="date"><span class="day">21</span><span class="month">SEP</span></div>
      <div class="news-body"><h4>General Young Women Meeting</h4><p>Westbrook, Elm Lane</p><p>12:30</p></div>
    </div>
  </section>
</main>

<footer class="site-footer">
  <p class="copyright">©2012 Vantrel 4 Management Limited. All Rights Reserved .Inc</p>
  <p class="legal"><a href="#">Terms of Use</a> | <a href="#">Privacy Policy</a></p>
  <div class="social">
    <span class="dot"></span>
    <span class="dot"></span>
    <svg width="34" height="26" viewBox="0 0 34 26" aria-label="Email"><rect x="1" y="1" width="32" height="24" fill="none" stroke="#eee" stroke-width="2.5"/><path d="M1 1l16 13L33 1M1 25l12-12M33 25L21 13" fill="none" stroke="#eee" stroke-width="2.5"/></svg>
    <svg width="28" height="28" viewBox="0 0 28 28" aria-label="Print"><rect x="7" y="2" width="14" height="8" fill="#eee"/><rect x="2" y="10" width="24" height="11" rx="2" fill="#eee"/><rect x="7" y="17" width="14" height="9" fill="#eee" stroke="#111" stroke-width="1.5"/></svg>
    <svg width="28" height="28" viewBox="0 0 28 28" aria-label="More"><path d="M14 2v24M2 14h24" stroke="#eee" stroke-width="5"/></svg>
  </div>
</footer>
</body>
</html>
```